UI design for an iOS(iPhone) photo editing app

This design contest is to design the UI/screenshots of an iOS(iPhone) app named "Vivid Lantern". Some minor design details are left out at this point as the mockup is still in progress. The icon of this app will be designed separately. The winner of this job will be selected to work on a long term basis as an iPad version and several updates will have to be designed as well as the Android version. Please take
this as a long term opportunity.
The photo app is called "Vivid Lantern". The design need to dynamic, different that stands out WITH a serious and polished look.
All the mockups and sample screenshots are attached for ease. Please thoroughly review them.
This app has the following screens:
1. Welcome screen(just a simple background will do now as icon will be put later).
2. Main Screen (or LightBox)
The background of this screen can be the same as the background of the welcome screen. It can be a wooden background OR a background of your
choice that fits and blends in the buttons and fonts/colors.
The main screen has this bars/buttons/options that has separate screens:
On top, menu bar:
has these buttons
settings on the left(icon)
in the middle, 3 buttons (please check lightbox mockup and lightbox sample pics)
on the right, share icon(check share screen sample)
Our share options:
"Share" button screenshot:
Our share options:
Save
Email
Copy
Snapmoor
Friendloom
Pixbarn
Chirpset
in the middle, just background where the pictures would appear later after importing
or saving
at the bottom bar:
3 buttons:
Camera Roll(on the left)
Camera Button(middle)
Advanced Button(on the right)
2 versions of this screenshot need to be designed.
1. regular version with all the options
2. regular version plus the "steam effect" button showing up on top of the "Advanced" button(mockup with red lines)
3 separate screenshots need to be designed for the options"
settings screenshot(please check sample):
Gift Vivid Lantern to a friend
Rate/review in the Appvault
(space in between...so they are grouped)
Geotagiing(on/off)
Captured photos get location-specific information(these lines in smaller fonts)
Launch in Capture Mode(on/off)
Vivid Lantern is automatically lauched in camera mode
Autosave to Camera Roll(on/off)
Captured photos are directly saved to camera roll
Reset All Tutorials
Tap to reset all the tutorials
In the "Steam Effect" screen, please check the mockup
Top Bar: lightbox button(to go back), heading and Done button
Middle: Steam background(provided)
Bottom bar:
refresh button
droplets(when clicked on/off options show up on top, please check mockup)
finger size(when clicked 3 options show up)
steam density(when clicked 3 options show up)
Please use the buttons for the droplets, finger size and steam density from the steam effects button image provided)
(and also the background of this screenshot(in the middle) would be a steam screen which is provided. Please use the
steam background provided and you need to use the background in the middle, just omit the top and the bottom bar from the image)
Now back to the main(lightbox screen):
When Clicked on the "Camera" in the middle of the bottom bar, the capture mode screen shows up.
Please refer to the mockup first
There you will see the cancel button on the left
camera button in the middle
a small settings button on the right
and a filters button on the right
and the filters bar on the top
ours need to like this
please refer to capture mode sample 1
please refer to capture mode sample 2
please refer to capture mode sample 3
normal
Grid
timer(5/15/30 secs)
Edit Screen(check sample)
Edit options
Adjust:(displayed on a bar)
1. Left
2. Right
3. Horizontal
4. Vertical
5. Straightening
Crop:
None
Original
Golden
Freeform
Square
3:2
4:3
4:6
5:7
8:10
16:9
Filters:(please note that this filter icon and the filter icon in the "capture mode" screenshot need to same)
(the filters are displayed on a bar, please check sample)
There is a sample picture that you need to put in the picture of the filters. It would be same picture in
every filter at this point.
00.None
0.Calibrate
1. aurora
2. drizzle
3. icicle
4. blizzard
5. calm
6. dew
7. knot
8. dry
9. eye
10. flurry
11. fog
12. frost
13. hail
14. haze
15. heat
16. humid
17. overcast
18. polar
19. thermal
20. trace
Editing options on top:(check sample)
Brightness
Contrast
Saturation
Textures:(dispalyed on a bar, check sample)
1.None
2.Bark
3.Grunge1
4.Grunge2
5.grunge3
6.Grunge4
7.Paper
8.Cardboard
9.Wood
10.Bokeh
11.Bricks
12.Metal
13.Asphalt
14.Pavement1
15.Pavement2
16.Paint1
17.Paint2
18.Rust
19.Towel
20.Stone1
21.Stone2
22.Wall
23.Urban1
24.Urban2
25.Urban3
26.Watercolor
Tilt-shift/Vignette:(check sample)
Borders:(check samples, at this point, we are working on them, you just need to make a bar that displays them)
1.None
2.
3.
4.
5.
6.
7.
8.
9.
10.
11.
12.
13.
14.
15.
16.
This is our primary design mockup. Upon selecting the final version, we will be working on some more and minor details(as
we are also working with the coders).
And there is a folder callled "app sample". Please take a look at it and think how our app can be different and stand out.
Thanks and feel free to contact me anytime if you have any questions. Looking forward to hearing from you and building a long term
relationship.
All camera app users who likes to edit their photos with cool tools.
Building

```html
<!DOCTYPE html>
<html lang="en">
<head>
<meta charset="utf-8">
<title>Vivid Lantern – Lightbox</title>
<link href="https://fonts.googleapis.com/css2?family=Open+Sans:wght@400;600;700&display=swap" rel="stylesheet">
<style>
  :root {
    --status-bg: #000000;
    --bar-bg-top: #1d1d1d;
    --bar-bg-bottom: #151515;
    --bar-line: #050505;
    --screen-bg: #161616;
    --screen-glow: #1c1c1c;
    --button-bg: #161616;
    --button-edge: #2a2a2a;
    --icon: #f2f2f2;
    --tab-bg: #222222;
    --tab-edge: #303030;
    --title: #e6e6e6;
  }
  * { margin: 0; padding: 0; box-sizing: border-box; }
  html, body { width: 800px; height: 1200px; overflow: hidden; background: var(--screen-bg); }
  body { font-family: "Open Sans", Arial, sans-serif; position: relative; }

  .status-bar {
    position: absolute; left: 0; top: 0; width: 800px; height: 50px;
    background: var(--status-bg); color: #fff;
  }
  .status-bar .signal { position: absolute; left: 10px; top: 14px; }
  .status-bar .carrier {
    position: absolute; left: 66px; top: 4px; font-size: 32px; font-weight: 600; letter-spacing: -0.5px;
  }
  .status-bar .battery { position: absolute; right: 7px; top: 12px; }

  .menu-bar {
    position: absolute; left: 0; top: 50px; width: 800px; height: 103px;
    background: linear-gradient(var(--bar-bg-top), var(--bar-bg-bottom));
    border-bottom: 2px solid var(--bar-line);
  }
  .menu-button {
    position: absolute; top: 14px; width: 88px; height: 72px;
    background: var(--button-bg); border: 1px solid var(--button-edge); border-radius: 6px;
    display: flex; align-items: center; justify-content: center;
  }
  .menu-button.settings { left: 40px; }
  .menu-button.share { left: 675px; }
  .view-toggle { position: absolute; left: 328px; top: 38px; }

  .lightbox {
    position: absolute; left: 0; top: 153px; width: 800px; height: 981px;
    background: radial-gradient(ellipse at 50% 35%, var(--screen-glow), var(--screen-bg) 70%);
  }
  .app-title {
    position: absolute; left: 0; top: 440px; width: 800px; text-align: center;
    font-size: 92px; font-weight: 400; color: var(--title); letter-spacing: -1px; line-height: 1;
  }

  .bottom-bar {
    position: absolute; left: 0; top: 1134px; width: 800px; height: 66px;
    background: linear-gradient(#1b1b1b, #111);
    border-top: 1px solid #262626;
  }
  .tab {
    position: absolute; width: 178px; height: 150px;
    background: linear-gradient(var(--tab-bg), #161616);
    border: 1px solid var(--tab-edge); border-radius: 8px 8px 0 0;
  }
  .tab.camera-roll { left: 130px; top: 1075px; }
  .tab.capture { left: 311px; top: 1058px; }
  .tab.advanced { left: 493px; top: 1075px; }
  .tab-button {
    position: absolute; left: 16px; top: 15px; width: 146px; height: 150px;
    background: linear-gradient(#1e1e1e, #151515);
    border: 1px solid #2e2e2e; border-radius: 8px;
    display: flex; justify-content: center; padding-top: 28px;
  }
  .tab.capture .tab-button { padding-top: 28px; }
  .tab.camera-roll .tab-button, .tab.advanced .tab-button { padding-top: 42px; }
</style>
</head>
<body>
  <header class="status-bar">
    <svg class="signal" width="48" height="24" viewBox="0 0 48 24" aria-hidden="true">
      <rect x="0" y="16" width="6" height="8" fill="#fff"/>
      <rect x="9" y="13" width="6" height="11" fill="#fff"/>
      <rect x="18" y="10" width="6" height="14" fill="#fff"/>
      <rect x="27" y="6" width="6" height="18" fill="#fff"/>
      <rect x="36" y="2" width="6" height="22" fill="#fff"/>
    </svg>
    <span class="carrier">Northwave</span>
    <svg class="battery" width="54" height="26" viewBox="0 0 54 26" aria-hidden="true">
      <rect x="1.5" y="1.5" width="46" height="23" rx="3" fill="none" stroke="#fff" stroke-width="2.5"/>
      <rect x="5" y="5" width="39" height="16" fill="#fff"/>
      <rect x="49" y="8" width="4" height="10" fill="#fff"/>
    </svg>
  </header>

  <nav class="menu-bar">
    <div class="menu-button settings" aria-label="Settings">
      <svg width="40" height="40" viewBox="0 0 40 40" aria-hidden="true">
        <g fill="var(--icon)">
          <circle cx="20" cy="20" r="12"/>
          <g>
            <rect x="17" y="3" width="6" height="34" rx="1"/>
            <rect x="17" y="3" width="6" height="34" rx="1" transform="rotate(45 20 20)"/>
            <rect x="17" y="3" width="6" height="34" rx="1" transform="rotate(90 20 20)"/>
            <rect x="17" y="3" width="6" height="34" rx="1" transform="rotate(135 20 20)"/>
          </g>
        </g>
        <circle cx="20" cy="20" r="5" fill="#161616"/>
      </svg>
    </div>

    <svg class="view-toggle" width="144" height="30" viewBox="0 0 144 30" aria-label="Grid or single view">
      <g fill="#fff">
        <rect x="3" y="6" width="7" height="7"/><rect x="15" y="6" width="7" height="7"/>
        <rect x="3" y="18" width="7" height="7"/><rect x="15" y="18" width="7" height="7"/>
      </g>
      <rect x="43" y="5" width="62" height="22" rx="11" fill="#0c0c0c" stroke="#2b2b2b"/>
      <defs>
        <radialGradient id="knob" cx="40%" cy="35%" r="70%">
          <stop offset="0" stop-color="#ffffff"/><stop offset="1" stop-color="#9a9a9a"/>
        </radialGradient>
      </defs>
      <circle cx="86" cy="16" r="13" fill="url(#knob)"/>
      <rect x="122" y="5" width="19" height="21" fill="#0c0c0c" stroke="#333"/>
    </svg>

    <div class="menu-button share" aria-label="Share">
      <svg width="40" height="44" viewBox="0 0 40 44" aria-hidden="true">
        <path d="M14 40 C 6 30, 8 16, 22 14 L 22 6 L 36 18 L 22 30 L 22 21 C 14 22, 11 30, 14 40 Z" fill="var(--icon)"/>
      </svg>
    </div>
  </nav>

  <main class="lightbox">
    <h1 class="app-title">Vivid Lantern</h1>
  </main>

  <footer class="bottom-bar"></footer>

  <div class="tab camera-roll" aria-label="Camera roll">
    <div class="tab-button">
      <svg width="64" height="48" viewBox="0 0 64 48" aria-hidden="true">
        <path d="M4 10 H18 L23 3 H41 L46 10 H60 V46 H4 Z" fill="var(--icon)"/>
        <circle cx="32" cy="28" r="14" fill="#151515"/>
        <circle cx="32" cy="28" r="9" fill="var(--icon)"/>
      </svg>
    </div>
  </div>

  <div class="tab advanced" aria-label="Advanced">
    <div class="tab-button">
      <svg width="72" height="64" viewBox="0 0 72 64" aria-hidden="true">
        <g fill="var(--icon)">
          <g transform="translate(30 14)">
            <circle r="9"/>
            <rect x="-2.5" y="-13" width="5" height="26"/>
            <rect x="-2.5" y="-13" width="5" height="26" transform="rotate(45)"/>
            <rect x="-2.5" y="-13" width="5" height="26" transform="rotate(90)"/>
            <rect x="-2.5" y="-13" width="5" height="26" transform="rotate(135)"/>
          </g>
          <g transform="translate(14 40)">
            <circle r="9"/>
            <rect x="-2.5" y="-13" width="5" height="26"/>
            <rect x="-2.5" y="-13" width="5" height="26" transform="rotate(45)"/>
            <rect x="-2.5" y="-13" width="5" height="26" transform="rotate(90)"/>
            <rect x="-2.5" y="-13" width="5" height="26" transform="rotate(135)"/>
          </g>
          <g transform="translate(46 40)">
            <circle r="14"/>
            <rect x="-3.5" y="-20" width="7" height="40"/>
            <rect x="-3.5" y="-20" width="7" height="40" transform="rotate(45)"/>
            <rect x="-3.5" y="-20" width="7" height="40" transform="rotate(90)"/>
            <rect x="-3.5" y="-20" width="7" height="40" transform="rotate(135)"/>
          </g>
        </g>
        <g fill="#151515">
          <circle cx="30" cy="14" r="4"/><circle cx="14" cy="40" r="4"/><circle cx="46" cy="40" r="6"/>
        </g>
      </svg>
    </div>
  </div>

  <div class="tab capture" aria-label="Capture">
    <div class="tab-button">
      <svg width="68" height="64" viewBox="0 0 68 64" aria-hidden="true">
        <g fill="none" stroke="var(--icon)" stroke-width="6">
          <path d="M3 20 V3 H20"/>
          <path d="M48 3 H65 V20"/>
          <path d="M3 44 V61 H20"/>
          <path d="M48 61 H65 V44"/>
        </g>
      </svg>
    </div>
  </div>
</body>
</html>
```